Theo Brandvik Photography
Theo Brandvik Photography's Homepage
Photography
Professional photographer
top
Overall look and feel should come from logo design.

```html
<!DOCTYPE html>
<html lang="en">
<head>
<meta charset="utf-8">
<title>Theo Brandvik Photography</title>
<link href="https://fonts.googleapis.com/css2?family=Questrial&display=swap" rel="stylesheet">
<style>
  :root {
    --page-bg: #ffffff;
    --ink: #3c3c3c;
    --muted: #8a8a8a;
    --nav-ink: #7a7a7a;
    --tile-border: #dcdcdc;
    --caption-bg: rgba(255,255,255,0.78);
    --caption-ink: #555555;
    --mark: #4a4a4a;
  }
  * { margin: 0; padding: 0; box-sizing: border-box; }
  html, body {
    width: 1200px; height: 901px; overflow: hidden;
    background: var(--page-bg);
    font-family: "Questrial", Arial, sans-serif;
  }
  .page { position: relative; width: 1200px; height: 901px; }

  .brand {
    position: absolute; right: 138px; top: 126px;
    display: flex; align-items: center; gap: 12px;
    color: var(--ink); font-size: 30px; letter-spacing: -0.5px;
  }
  .brand-square { width: 40px; height: 40px; background: var(--mark); }

  .gallery {
    position: absolute; left: 120px; top: 245px;
    display: grid;
    grid-template-columns: repeat(4, 228px);
    grid-template-rows: repeat(3, 142px);
    column-gap: 9px; row-gap: 5px;
  }
  .tile {
    position: relative; border: 2px solid var(--tile-border);
    overflow: hidden;
  }
  .tile-photo { position: absolute; inset: 0; }
  .tile-caption {
    position: absolute; left: 0; right: 0; bottom: 0; height: 24px;
    background: var(--caption-bg);
    color: var(--caption-ink); font-size: 14px;
    text-align: center; line-height: 24px;
  }

  .copyright {
    position: absolute; right: 137px; top: 706px;
    color: var(--muted); font-size: 13px;
  }
  .main-nav {
    position: absolute; left: 127px; top: 774px;
    display: flex; gap: 10px;
    color: var(--nav-ink); font-size: 13px;
  }
  .main-nav .sep { color: var(--muted); }
</style>
</head>
<body>
<div class="page">
  <div class="brand"><span class="brand-square"></span><span class="brand-name">Theo Brandvik Photography</span></div>

  <div class="gallery">
    <div class="tile"><div class="tile-photo" role="img" aria-label="Baby portrait in soft light" style="background:linear-gradient(135deg,#f4ede4,#e9d8c6)"></div><div class="tile-caption">Babies</div></div>
    <div class="tile"><div class="tile-photo" role="img" aria-label="Child with yellow umbrella by brick wall" style="background:linear-gradient(180deg,#a65c45 0%,#8c4a38 55%,#d9b23a 100%)"></div><div class="tile-caption">Children</div></div>
    <div class="tile"><div class="tile-photo" role="img" aria-label="Family standing together in matching blue shirts" style="background:linear-gradient(180deg,#eceef0,#8ea3bb 60%,#5e6f86)"></div><div class="tile-caption">Family</div></div>
    <div class="tile"><div class="tile-photo" role="img" aria-label="Senior portrait by a pale wall" style="background:linear-gradient(135deg,#f3ece2,#d9cbb8)"></div><div class="tile-caption">Seniors</div></div>

    <div class="tile"><div class="tile-photo" role="img" aria-label="Wedding couple embracing, black and white" style="background:linear-gradient(135deg,#e8e8e8,#8e8e8e)"></div><div class="tile-caption">Owen &amp; Lena</div></div>
    <div class="tile"><div class="tile-photo" role="img" aria-label="Bride and groom outdoors, black and white" style="background:linear-gradient(135deg,#d6d6d6,#6f6f6f 60%,#cfcfcf)"></div><div class="tile-caption">Reid &amp; Marla</div></div>
    <div class="tile"><div class="tile-photo" role="img" aria-label="Couple standing in a dark doorway" style="background:radial-gradient(circle at 50% 45%,#e4dcd2,#5a4435 60%,#2e221a)"></div><div class="tile-caption">Casey &amp; Wren</div></div>
    <div class="tile"><div class="tile-photo" role="img" aria-label="Couple on a beach boardwalk" style="background:linear-gradient(180deg,#d4e6ea,#b8cfc9 55%,#d9cdb4)"></div><div class="tile-caption">Grant &amp; Elise</div></div>

    <div class="tile"><div class="tile-photo" role="img" aria-label="Wedding couple among green trees" style="background:linear-gradient(135deg,#9fb27a,#e6eadf 50%,#7d915c)"></div><div class="tile-caption">Dean &amp; Carly</div></div>
    <div class="tile"><div class="tile-photo" role="img" aria-label="Bride in a field, sepia tones" style="background:linear-gradient(135deg,#8a7a5c,#c9bb98 55%,#6b5c44)"></div><div class="tile-caption">Nora &amp; Kyle</div></div>
    <div class="tile"><div class="tile-photo" role="img" aria-label="Fashion model in bright colourful room" style="background:linear-gradient(135deg,#e9b7a8,#f3e3b8 50%,#d98a94)"></div><div class="tile-caption">Fashion</div></div>
    <div class="tile"><div class="tile-photo" role="img" aria-label="Bridal portrait in warm sepia" style="background:linear-gradient(135deg,#e8dccb,#b69c7c)"></div><div class="tile-caption">Hanna Bridal</div></div>
  </div>

  <p class="copyright">Copyright © 2010-2011, TheoBrandvikPhotography.com</p>

  <nav class="main-nav">
    <span>HOME</span><span class="sep">|</span>
    <span>ABOUT US</span><span class="sep">|</span>
    <span>SERVICE</span><span class="sep">|</span>
    <span>GALLERY</span><span class="sep">|</span>
    <span>BLOG</span><span class="sep">|</span>
    <span>CONTACT US</span>
  </nav>
</div>
</body>
</html>
```